Need new clean look for BrightHarborLane.com Homepage

Looking for a complete redesign of our homepage that will be built on Bootstrap 4. Our current page exists at www.brightharborlane.com
The layout is fairly simple with a new header, footer, and two column layout. The header features a top slim nav with event names, our logo, main navigation and a fighter search field. The right column features several content widgets and the left column (or main content area) features two columns of dynamically sized content boxes. Those boxes will feature seven different types of content and the containing box should be designed to clearly indicate the type of content (Editorial Blog, External Link, Embedded Video, Quick News Text, QZ Post, Lumagrid Post, Vexlo Post). These content boxes will also be numbered sequentially.
Mixed Martial Arts, Sports
1 page

```html
<!DOCTYPE html>
<html lang="en">
<head>
<meta charset="utf-8">
<title>BrightHarborLane – Home</title>
<link rel="stylesheet" href="https://fonts.googleapis.com/css2?family=Roboto:wght@400;500;700;900&display=swap">
<style>
:root{
  --red:#d0112b;
  --red-dark:#a10b20;
  --ink:#222;
  --text:#444;
  --muted:#888;
  --line:#e2e2e2;
  --page:#f2f2f2;
  --card:#fff;
  --ad:#d5d5d5;
  --qz:#3b5998;
  --vexlo:#55acee;
  --video:#e62117;
  --luma:#c13584;
}
*{box-sizing:border-box;margin:0;padding:0}
html,body{width:1200px;height:2725px;overflow:hidden}
body{font-family:"Roboto",Arial,sans-serif;background:var(--page);color:var(--text);position:relative}
.abs{position:absolute}
/* top bar */
.event-bar{left:0;top:0;width:1200px;height:40px;background:var(--red);display:flex;align-items:center;font-size:13px;color:#fff;font-weight:500}
.event-bar .label{background:var(--red-dark);height:40px;display:flex;align-items:center;padding:0 26px 0 85px;font-weight:700}
.event-bar .event{padding:0 22px}
/* header */
.site-header{left:0;top:40px;width:1200px;height:84px;background:#fff;box-shadow:0 1px 3px rgba(0,0,0,.08);display:flex;align-items:center}
.logo{position:absolute;left:85px;top:28px;font-size:27px;font-weight:900;color:var(--red);letter-spacing:1px;text-transform:uppercase;display:flex;align-items:center;gap:10px}
.logo .mark{width:24px;height:24px;background:var(--red)}
.main-nav{position:absolute;right:85px;top:32px;display:flex;gap:44px;font-size:18px;font-weight:500;color:var(--ink);align-items:center}
.main-nav .active{color:var(--red)}
.ad{background:var(--ad);color:#9a9a9a;display:flex;align-items:center;justify-content:center;font-size:24px}
/* section heading */
.section-title{font-size:21px;font-weight:700;color:var(--red);text-transform:uppercase;letter-spacing:.5px}
.section-title span{color:var(--ink)}
.title-rule{height:2px;background:var(--line)}
.title-rule i{display:block;height:3px;background:var(--red);margin-top:-.5px}
/* cards */
.card{background:var(--card);box-shadow:0 1px 4px rgba(0,0,0,.1);display:flex;flex-direction:column}
.card-head{display:flex;align-items:center;height:50px;padding-right:12px;flex:none}
.rank{background:var(--red);color:#fff;font-weight:700;font-size:14px;height:26px;min-width:40px;display:flex;align-items:center;justify-content:center;padding:0 6px}
.rank sup{font-size:9px}
.card-title{flex:1;padding-left:12px;font-size:13px;font-weight:500;color:var(--ink);line-height:1.3}
.type{width:24px;height:24px;flex:none}
.type.qz{background:var(--qz);border-radius:3px}
.type.vexlo{background:var(--vexlo);border-radius:50%}
.type.video{background:var(--video);border-radius:6px;height:18px;width:26px}
.type.luma{background:var(--luma);border-radius:6px;width:22px;height:22px}
.media{flex:none}
.img-gym{background:linear-gradient(135deg,#6b4a3a,#c79873 55%,#3a2a22)}
.img-road{background:linear-gradient(160deg,#9bb2c6,#c9b08d 60%,#6d6a5a)}
.img-arena{background:linear-gradient(160deg,#2a2a2a,#8a7a6a 50%,#222)}
.img-poster{background:linear-gradient(90deg,#111,#3b3b3b 50%,#111)}
.img-fight{background:linear-gradient(150deg,#9e6c55,#c8b6a6 50%,#4a4a4a)}
.img-cage{background:linear-gradient(140deg,#1c2634,#6b7d93 55%,#2b2b2b)}
.img-gold{background:linear-gradient(135deg,#2a1f16,#a07550 50%,#3a2a1e)}
.img-portrait{background:linear-gradient(180deg,#cfcfcf,#8b7d74 60%,#dedede)}
.byline{display:flex;justify-content:space-between;font-size:10px;color:var(--muted);padding:16px 20px 8px;text-transform:uppercase}
.excerpt{font-size:12px;line-height:1.55;color:var(--text);padding:4px 20px 0}
.more{font-size:11px;color:var(--red);text-align:right;padding:6px 20px 0}
.source{font-size:11px;color:var(--muted);padding:14px 20px}
.source b{color:var(--red);font-weight:500}
/* embedded posts */
.embed{margin:0 16px;border:1px solid var(--line);border-radius:4px;padding:10px;font-size:10px;color:var(--text);line-height:1.45}
.who{display:flex;align-items:center;gap:8px;margin-bottom:8px}
.avatar{width:26px;height:26px;border-radius:50%;background:#8b8b8b;flex:none}
.who b{color:var(--qz);font-size:10px}
.who small{display:block;color:var(--muted);font-size:8px}
.actions{display:flex;gap:22px;font-size:9px;color:#666;padding:8px 0 4px;border-top:1px solid var(--line);margin-top:8px}
.link-blue{color:var(--qz)}
.dots{display:flex;gap:5px;margin-top:8px}
.dots i{width:13px;height:13px;border-radius:50%;background:#e4e4e4;display:block}
/* right widgets */
.widget{background:#fff;box-shadow:0 1px 4px rgba(0,0,0,.1);padding:22px 22px}
.widget .section-title{font-size:15px}
.headline{display:flex;gap:12px;font-size:13px;color:var(--ink);font-weight:500;line-height:1.45;padding:16px 0;border-bottom:1px solid var(--line)}
.headline time{color:#666;font-weight:400;flex:none}
.headline:last-child{border:none}
.fe-title{text-align:center;font-size:14px;font-weight:500;color:var(--ink);margin-top:20px}
.fe-title em{font-style:normal;color:var(--red)}
.fe-date{text-align:center;font-size:11px;color:var(--muted);margin-top:4px}
.fe-names{display:flex;justify-content:space-between;font-size:12px;font-weight:500;color:var(--ink);margin-top:10px;padding:0 14px}
.fe-names em{font-style:normal;color:var(--red)}
table.record{width:100%;margin-top:18px;font-size:11px;border-collapse:collapse}
table.record td{text-align:center;padding:7px 0}
table.record td:first-child{color:#2b9a3e}
table.record td:nth-child(2){color:var(--red);font-weight:500}
table.record td:last-child{color:#666}
.fe-result{text-align:center;font-size:13px;font-weight:700;color:#555;margin-top:16px}
.fe-result span{font-weight:400}
.remix-cap{display:flex;justify-content:space-between;font-size:10px;color:var(--ink);font-weight:500;margin-top:6px}
.remix-cap em{font-style:normal;color:var(--red);font-size:9px;text-align:center;line-height:1.1}
/* footer */
.site-footer{left:0;top:2403px;width:1200px;height:322px;background:#fff}
.f-logo{font-size:18px;font-weight:900;color:var(--red);text-transform:uppercase;letter-spacing:.5px}
.f-text{font-size:13px;color:#9a9a9a;line-height:1.6;margin-top:14px;width:290px}
.f-social{display:flex;gap:24px;margin-top:26px}
.f-social i{width:24px;height:24px;background:#cfcfcf;border-radius:4px;display:block}
.f-head{font-size:16px;color:var(--red);font-weight:500}
.f-links{display:grid;grid-template-columns:130px 130px;font-size:14px;color:#888;line-height:1.7;margin-top:12px}
.f-contact{font-size:14px;color:#888;line-height:1.7;margin-top:12px}
.f-bottom{left:85px;top:270px;width:1028px;border-top:1px solid var(--line);padding-top:20px;display:flex;justify-content:space-between;font-size:11px;color:#aaa}
.f-bottom span{color:#666}
</style>
</head>
<body>

<div class="abs event-bar">
  <div class="label">Upcoming Events</div>
  <div class="event">Sat. 2/8 - Vanta FC 124 (Los Angeles, CA)</div>
  <div class="event">Fri, 2/16 - Ironclad 124 (St. Louis, MO)</div>
  <div class="event">Sat. 2/7 - Vanta FC FIGHT NIGHT 126 (Belem, Brazil)</div>
  <div class="event">Sat. 4/7 - Vanta FC 2</div>
</div>

<header class="abs site-header">
  <div class="logo"><span class="mark"></span>BrightHarborLane</div>
  <nav class="main-nav">
    <span class="active">News</span><span>Forums</span><span>Events</span><span>Fighters</span><span>Account</span>
    <svg width="18" height="18" viewBox="0 0 18 18" fill="none" stroke="#333" stroke-width="2"><circle cx="7.5" cy="7.5" r="5.5"/><path d="M11.5 11.5L16 16"/></svg>
  </nav>
</header>

<div class="abs ad" style="left:85px;top:150px;width:1028px;height:166px">Ad</div>

<!-- Trending -->
<h2 class="abs section-title" style="left:85px;top:383px">Trending <span>Content</span></h2>
<div class="abs title-rule" style="left:85px;top:422px;width:712px"><i style="width:220px"></i></div>

<!-- 1 editorial -->
<article class="abs card" style="left:85px;top:455px;width:353px;height:367px">
  <div class="card-head"><span class="rank">1<sup>st</sup></span><span class="card-title">Marlow Self-imposes concussion protocol</span>
    <svg class="type" viewBox="0 0 24 24" fill="none" stroke="#333" stroke-width="2"><rect x="2" y="4" width="20" height="16"/><path d="M6 9h6v5H6zM15 9h4M15 13h4M6 17h13"/></svg></div>
  <div class="media img-gym" role="img" aria-label="Fighter with tattooed back wearing red headgear in a gym" style="height:182px"></div>
  <div class="byline"><span>By Harold Penn</span><span>02/01/2018</span></div>
  <p class="excerpt">Jim Marlow: "It sucks sometimes being on the sidelines, and feeling like, 'Oh, I could train right now.' But you can't. You have to give your brain time to rest."</p>
  <p class="more">Read More</p>
</article>

<!-- 3 vexlo -->
<article class="abs card" style="left:85px;top:838px;width:353px;height:467px">
  <div class="card-head"><span class="rank">3<sup>rd</sup></span><span class="card-title">Okada wins main event</span><span class="type vexlo"></span></div>
  <div class="embed" style="padding:12px">
    <div class="who"><span class="avatar" style="background:#111"></span><div><b style="color:#222">Vanta FC</b><small>@vantafc</small></div></div>
    <p style="font-size:13px;color:#222;line-height:1.35">Okada seals the victory in front of his home crowd: <span style="color:var(--red)">vnt.ly/2s9L61l</span></p>
    <div class="img-arena" role="img" aria-label="Winning fighter raising both arms in the cage" style="height:186px;margin-top:8px"></div>
    <p style="font-size:8px;color:var(--muted);margin-top:8px">8:26 AM - 18 Jul 2017</p>
    <div style="display:flex;align-items:center;gap:10px;margin-top:6px;font-size:8px"><span><b>2,194</b> Retweets</span><span><b>8,812</b> Likes</span><span class="dots" style="margin:0"><i></i><i></i><i></i><i></i><i></i><i></i><i></i><i></i></span></div>
    <div class="actions" style="font-size:8px"><span>891</span><span>2.2K</span><span>8.8K</span></div>
    <div style="border-top:1px solid var(--line);margin:4px -12px -12px;padding:8px 12px;background:#f7f9fa;display:flex;gap:8px;align-items:center;font-size:8px;color:var(--muted)"><span class="avatar" style="width:16px;height:16px"></span>Tweet your reply</div>
  </div>
</article>

<!-- 6 external -->
<article class="abs card" style="left:85px;top:1316px;width:353px;height:293px">
  <div class="card-head" style="height:64px"><span class="rank">6<sup>th</sup></span><span class="card-title">Whitford: Salgado's legacy is definitely tarnished</span>
    <svg class="type" viewBox="0 0 24 24" fill="none" stroke="#333" stroke-width="2"><path d="M19 14v7H3V5h7M14 3h7v7M21 3L11 13"/></svg></div>
  <div class="media img-cage" role="img" aria-label="Two fighters trading strikes inside the cage" style="height:182px"></div>
  <p class="source">Source: <b>cagereport.com</b></p>
</article>

<!-- 7 editorial -->
<article class="abs card" style="left:85px;top:1629px;width:353px;height:351px">
  <div class="card-head"><span class="rank">7<sup>th</sup></span><span class="card-title">Swift Hawk: Why I am the P4P best</span>
    <svg class="type" viewBox="0 0 24 24" fill="none" stroke="#333" stroke-width="2"><rect x="2" y="4" width="20" height="16"/><path d="M6 9h6v5H6zM15 9h4M15 13h4M6 17h13"/></svg></div>
  <div class="media img-gold" role="img" aria-label="Shirtless fighter posing by the cage fence" style="height:182px"></div>
  <div class="byline"><span>By Harold Penn</span><span>02/01/2018</span></div>
  <p class="excerpt">Darius Jordan: "The reason I have that label is my longevity as a champion and dominating higher competition."</p>
  <p class="more">Read More</p>
</article>

<!-- 2 qz -->
<article class="abs card" style="left:446px;top:455px;width:351px;height:430px">
  <div class="card-head"><span class="rank">2<sup>nd</sup></span><span class="card-title">Brandt Injured, out of Vanta FC 222</span><span class="type qz"></span></div>
  <div class="embed">
    <div class="who"><span class="avatar"></span><div><b>Harold Penn</b><small>Today at 19:33</small></div></div>
    <p style="font-size:9px">Vanta FC featherweight champion Max 'Steady' Brandt injured his ankle while sparring this week, and he will miss his third title defense vs Ronnie Vale at Vanta FC 222.</p>
    <p class="link-blue" style="font-size:8px">See translation</p>
    <div class="img-road" role="img" aria-label="Shirtless fighter running on a country road" style="height:164px;margin-top:6px"></div>
    <div class="actions"><span>Like</span><span>Comment</span><span>Share</span></div>
    <p style="font-size:8px;color:var(--muted)">34%</p>
    <div style="display:flex;gap:8px;align-items:center;background:#f6f7f9;padding:5px;margin-top:4px;font-size:8px;color:var(--muted)"><span class="avatar" style="width:14px;height:14px"></span>Write something...</div>
  </div>
</article>

<!-- 4 video -->
<article class="abs card" style="left:446px;top:905px;width:351px;height:233px">
  <div class="card-head"><span class="rank">4<sup>th</sup></span><span class="card-title">Free Fight: Whitford vs. Stonecrest</span><span class="type video"></span></div>
  <div class="media img-poster" role="img" aria-label="Fight poster of two fighters facing off, Ravelo vs Stonecrest, Feb 10" style="height:183px"></div>
</article>

<!-- 5 lumagrid -->
<article class="abs card" style="left:446px;top:1147px;width:351px;height:589px">
  <div class="card-head"><span class="rank">5<sup>th</sup></span><span class="card-title">Whitaker blasts Nakamura</span><span class="type luma"></span></div>
  <div class="embed" style="padding:0">
    <div class="who" style="padding:10px;margin:0"><span class="avatar"></span><b style="color:#222">deanwhitaker</b></div>
    <div class="img-fight" role="img" aria-label="Two female fighters exchanging punches in the octagon" style="height:304px"></div>
    <div style="padding:10px;font-size:9px">
      <div style="display:flex;justify-content:space-between;align-items:center"><span class="link-blue">View Insights</span><span style="background:#3897f0;color:#fff;padding:3px 16px;border-radius:2px">Promote</span></div>
      <div class="actions" style="border:none;gap:14px"><span>♡</span><span>○</span><span>➤</span></div>
      <p style="margin-top:6px;font-size:8px"><b>♥ leahfit, alexrun, and 294 others</b></p>
      <p style="font-size:8px"><b>deanwhitaker</b> Paula Carvalho, you showed so much heart and toughness in that fight. I'm honored to have you fight in the Vanta FC.</p>
      <p class="link-blue" style="font-size:8px">#boxing #deanwhitaker</p>
      <p style="font-size:8px;color:var(--muted)">View all 13 comments</p>
    </div>
  </div>
</article>

<!-- 8 qz video -->
<article class="abs card" style="left:446px;top:1763px;width:351px;height:549px">
  <div class="card-head"><span class="rank">8<sup>th</sup></span><span class="card-title">Brandt Injured, out of Vanta FC 222</span><span class="type qz"></span></div>
  <div class="embed">
    <div class="who"><span class="avatar"></span><div><b>Aaron Pike</b><small>Today at 19:33</small></div></div>
    <p style="font-size:9px">Brazil's regulatory body, CSRMA, has the right to fine 20% of show and win money, and split it 50-50 with the other fighter... <span class="link-blue">Read More</span></p>
    <p class="link-blue" style="font-size:8px">See translation</p>
    <div class="img-portrait" role="img" aria-label="Video still of a bearded fighter in a white shirt with taped hands" style="height:322px;margin-top:6px;position:relative">
      <div style="position:absolute;left:8px;right:8px;bottom:10px;height:3px;background:rgba(255,255,255,.6)"></div>
    </div>
    <div style="display:flex;justify-content:space-between;font-size:8px;color:var(--muted);margin-top:6px"><span>34%</span><span>2,475 comments · 1,689 shares</span></div>
    <div class="actions"><span>Like</span><span>Comment</span><span>Share</span></div>
  </div>
</article>

<!-- right column -->
<div class="abs ad" style="left:816px;top:355px;width:297px;height:245px">Ad</div>

<aside class="abs widget" style="left:816px;top:620px;width:297px;height:329px">
  <h3 class="section-title">Latest <span>Headlines</span></h3>
  <div class="title-rule" style="margin-top:10px"><i style="width:110px"></i></div>
  <div style="margin-top:6px">
    <div class="headline"><time>16:45</time><span>Sources: Harbor Hawks shifting free agent focus to.</span></div>
    <div class="headline"><time>16:30</time><span>Rays' Novak reaches 5,000 minute mark</span></div>
    <div class="headline"><time>16:20</time><span>Stags' Lorca hurls chair after ejections vs Monarchs</span></div>
    <div class="headline"><time>16:05</time><span>Tad Frazer inks deal with Comets, source say</span></div>
  </div>
</aside>

<aside class="abs widget" style="left:816px;top:996px;width:297px;height:431px">
  <h3 class="section-title">Featured <span>Event</span></h3>
  <div class="title-rule" style="margin-top:10px"><i style="width:90px"></i></div>
  <p class="fe-title">Vanta FC 223: Stonecrest <em>vs.</em> Ravelo</p>
  <p class="fe-date">February 10th, 2018 ( Perth, Australia)</p>
  <div class="img-fight" role="img" aria-label="Both fighters in front of their national flags" style="height:110px;margin-top:10px;background:linear-gradient(90deg,#2a4a9a,#c73a3a 45%,#e8e8e8 55%,#2a4a9a)"></div>
  <div class="fe-names"><span>Joel Ravelo</span><em>VS</em><span>Lucas Stonecrest</span></div>
  <table class="record">
    <tr><td>19-2</td><td>Record</td><td>15-4</td></tr>
    <tr><td>2</td><td>Win Streak</td><td>4</td></tr>
    <tr><td>1</td><td>Rank</td><td>2</td></tr>
  </table>
  <p class="fe-result">Bout Result: <span>TBD</span></p>
</aside>

<div class="abs ad" style="left:816px;top:1449px;width:297px;height:245px">Ad</div>

<aside class="abs widget" style="left:816px;top:1713px;width:297px;height:372px">
  <h3 class="section-title">Our <span>Remix</span></h3>
  <div class="title-rule" style="margin-top:10px"><i style="width:70px"></i></div>
  <div class="img-gold" role="img" aria-label="Fighter seated in a red-walled room" style="height:140px;margin-top:22px"></div>
  <div class="remix-cap"><span>The incredible Story of Elias Stone</span><em>980<br>Views</em></div>
  <div style="display:flex;gap:8px;margin-top:10px;overflow:hidden">
    <div class="img-arena" role="img" aria-label="Fighter on the mat" style="width:100px;height:60px;flex:none"></div>
    <div class="img-road" role="img" aria-label="Training session in a ring" style="width:100px;height:60px;flex:none"></div>
    <div class="img-cage" role="img" aria-label="Fight highlight" style="width:40px;height:60px;flex:none"></div>
  </div>
  <div class="remix-cap" style="justify-content:flex-start;gap:18px;white-space:nowrap"><span>Top Fighter <em>140</em></span><span>Best Training <em>240</em></span><span>Epic c</span></div>
</aside>

<!-- footer -->
<footer class="abs site-footer">
  <div class="abs" style="left:85px;top:40px">
    <div class="f-logo">BrightHarborLane</div>
    <p class="f-text">Lorem ipsum dolor sit amet, consectetur adipiscing elit. Proin ac diam non nulla pellentesque consect a a lectus. Cras pharetra ante.</p>
    <div class="f-social"><i></i><i></i><i></i><i></i><i></i></div>
  </div>
  <div class="abs" style="left:553px;top:38px">
    <h4 class="f-head">Quick Links</h4>
    <div class="f-links"><span>Home</span><span>Fighters</span><span>About</span><span>Create Account</span><span>Advertising</span><span>Login</span><span>News</span><span>Contact Us</span><span>Forums</span><span>FAQs</span><span>Events</span></div>
  </div>
  <div class="abs" style="left:934px;top:38px">
    <h4 class="f-head">Contact Us</h4>
    <div class="f-contact">88 Harbor Row, Westfield<br>MA 01085<br>(555) 014-2290<br><span style="display:block;margin-top:6px">hello@brightharborlane.com</span></div>
  </div>
  <div class="abs f-bottom"><span style="color:#aaa">© 2018 by Northpier Studio. All rights reserved.</span><span>Terms of Use &nbsp;&nbsp; Privacy Policy</span></div>
</footer>

</body>
</html>
```